Hip-Hop/Rap album needs artwork

I would like a design that parallels the ideas of beauty and flaws. My name is Varun Mehta and I'm titling it "Quiet Embers", this album is basically a collection of songs that have me trying to understand the good and evil in this world, how they run so close together at times. How they sometimes can be caused by the same source, or how sometimes we find beauty within all the ugliness we witness. Some subject matters include rape, serial killers, depression, the idea of love, the projection of women in the media, and the idea of dying prematurely.

Target Market(s)

Music listeners, who are looking for new music so artwork that will capture their eye and stand out, rough age estimate would be 17-35, people with time to kill.

Industry/Entity Type

Media

Font styles to use
Decorative
Script

Requirements
Must have
• please include my name VARUN MEHTA and the title QUIET EMBERS, preferably in different fonts

I'm going for something more moody and dark rather than something happy, so darker colors please.
Nice to have
• I would prefer to have a drawing or painting of some sort, to give some humanity to the design but not required.

```html
<!DOCTYPE html>
<html lang="en">
<head>
<meta charset="UTF-8">
<title>Varun Mehta – Quiet Embers</title>
<link rel="stylesheet" href="https://fonts.googleapis.com/css2?family=Anton&family=Playball&display=swap">
<style>
  :root {
    --frame-black: #000000;
    --frame-red: #c8202c;
    --bevel-top: #bd1d2c;
    --bevel-right: #dc1f2a;
    --bevel-bottom: #b91c2b;
    --bevel-left: #de1f2b;
    --ink: #000000;
    --ink-edge: #5a5a5a;
    --script-fill: #2f2b2c;
    --script-edge: #0d0d0d;
    --motif: #8f5a4c;
  }
  html, body {
    margin: 0;
    padding: 0;
    width: 1200px;
    height: 1200px;
    overflow: hidden;
    background: var(--frame-black);
  }
  .album-cover {
    display: block;
    width: 1200px;
    height: 1200px;
  }
  .artist-name {
    font-family: "Anton", "Impact", sans-serif;
    fill: var(--ink);
    stroke: var(--ink-edge);
    stroke-width: 4;
    paint-order: stroke;
  }
  .album-title {
    font-family: "Playball", "Brush Script MT", cursive;
    fill: var(--script-fill);
    stroke: var(--script-edge);
    stroke-width: 3;
    paint-order: stroke;
  }
  .bevel-top { fill: var(--bevel-top); }
  .bevel-right { fill: var(--bevel-right); }
  .bevel-bottom { fill: var(--bevel-bottom); }
  .bevel-left { fill: var(--bevel-left); }
  .frame-line { fill: none; stroke: var(--frame-red); stroke-width: 4; }
  .motif-area { fill: var(--motif); opacity: 0.45; }
</style>
</head>
<body>
<svg class="album-cover" viewBox="0 0 1200 1200" xmlns="http://www.w3.org/2000/svg">
  <rect x="0" y="0" width="1200" height="1200" fill="var(--frame-black)"/>
  <rect class="frame-line" x="9" y="9" width="1182" height="1182"/>

  <g class="bevel-panel">
    <polygon class="bevel-top" points="30,30 1170,30 600,600"/>
    <polygon class="bevel-right" points="1170,30 1170,1170 600,600"/>
    <polygon class="bevel-bottom" points="1170,1170 30,1170 600,600"/>
    <polygon class="bevel-left" points="30,1170 30,30 600,600"/>
  </g>

  <ellipse class="motif-area" cx="235" cy="725" rx="160" ry="175" role="img" aria-label="Faint star-shaped emblem with curved strokes around it"/>

  <text class="artist-name artist-first" x="72" y="492" font-size="500" textLength="1058" lengthAdjust="spacingAndGlyphs">Varun</text>
  <text class="artist-name artist-last" x="415" y="812" font-size="330" textLength="715" lengthAdjust="spacingAndGlyphs">Mehta</text>

  <text class="album-title" x="52" y="1080" font-size="200" textLength="1118" lengthAdjust="spacingAndGlyphs">Quiet Embers</text>
</svg>
</body>
</html>
```